marlow pennant website Redesign

Read the Company mission statement and then help us redesign the website along the guidelines in the design brief and using the logo and fonts supplied.

The current marlow pennant website is very dated but has been very sucessful, we would like to invest in a brand refresh and site rebuild to bring the website up to 2018 standard.

We have using cut and paste from other travel websites made a pdf mock up of what sort of content we need on the pages and the lay out we like.

Target Market(s)

+45 Plus experienced Marlow Pennant, established, educated

Number of Pages Required

4 page

Font styles to use
Sans Serif

Requirements
Must have
• There is a full brief document and mock up, it must follow the brand guidelines
Nice to have
• There is a full brief document and mock up
Should not have
• Looks of a cheap cruise deal travel site

```html
<!DOCTYPE html>
<html lang="en">
<head>
<meta charset="utf-8">
<title>Marlow Pennant – Travel with Personality</title>
<link href="https://fonts.googleapis.com/css2?family=Lato:wght@400;700;900&family=Open+Sans:ital,wght@0,400;0,600;0,700;1,400&display=swap" rel="stylesheet">
<style>
:root{
  --brand:#1f7fc2;
  --green:#4daa5a;
  --green-dark:#3d9549;
  --ink:#222;
  --text:#555;
  --muted:#8a8a8a;
  --line:#dcdcdc;
  --band:#e6eef7;
  --footer:#262626;
  --footer-text:#cfcfcf;
  --white:#fff;
}
*{box-sizing:border-box;margin:0;padding:0}
html,body{width:1200px;height:5202px;overflow:hidden}
body{position:relative;background:var(--white);font-family:"Open Sans",Arial,sans-serif;color:var(--text);font-size:14px}
.sec{position:absolute;left:0;width:1200px}
.abs{position:absolute}
h2.section-title{position:absolute;left:0;width:1200px;text-align:center;font-family:"Lato",Arial,sans-serif;font-weight:900;font-size:34px;color:var(--ink);letter-spacing:.5px}
.btn{display:inline-block;background:var(--green);color:var(--white);font-family:"Lato",Arial,sans-serif;font-weight:700;font-size:13px;letter-spacing:.6px;border-radius:24px;text-transform:uppercase;text-align:center}
.btn-outline{display:inline-block;border:2px solid var(--green);color:var(--green-dark);font-family:"Lato",Arial,sans-serif;font-weight:700;font-size:12px;letter-spacing:.6px;border-radius:24px;text-transform:uppercase;text-align:center;background:var(--white)}

/* header */
.header{top:0;height:104px}
.brand-name{left:98px;top:20px;font-family:"Lato",Arial,sans-serif;font-weight:900;font-size:34px;color:var(--brand);letter-spacing:1px;line-height:1}
.brand-sub{left:98px;top:60px;font-family:"Lato",Arial,sans-serif;font-weight:900;font-size:17px;color:var(--brand);letter-spacing:3px;text-transform:uppercase}
.header-phone{left:494px;top:43px;font-weight:600;font-size:16px;color:var(--ink);display:flex;align-items:center;gap:8px}
.social{display:flex;gap:10px}
.social span{width:34px;height:34px;border-radius:50%;background:var(--brand);display:block}
.header .social{left:652px;top:35px}
.header .btn{left:874px;top:33px;width:226px;height:40px;line-height:40px}

/* nav */
.nav{top:104px;height:52px;border-top:1px solid var(--line);border-bottom:1px solid var(--line)}
.nav ul{list-style:none;display:flex;position:absolute;left:98px;top:0;height:50px;align-items:center}
.nav li{font-family:"Lato",Arial,sans-serif;font-weight:700;font-size:14.5px;color:var(--ink);margin-right:44px}
.nav li.current{color:var(--green)}
.nav li:last-child{margin-right:0}

/* hero */
.hero{top:156px;height:520px;background:linear-gradient(180deg,#7fa6b4 0%,#5f8e9a 45%,#3f6c73 100%)}
.hero h1{position:absolute;left:0;width:1200px;top:182px;text-align:center;font-family:"Lato",Arial,sans-serif;font-weight:900;font-size:48px;color:var(--white);letter-spacing:1.5px}
.hero-search{left:291px;top:274px;width:618px;height:50px;background:var(--white);display:flex;align-items:center}
.hero-search .field{flex:1;padding-left:18px;font-size:14px;color:var(--muted);display:flex;align-items:center;gap:10px}
.hero-search .go{width:60px;height:50px;background:var(--green);display:flex;align-items:center;justify-content:center}
.hero-dots{left:570px;top:462px;display:flex;gap:8px}
.hero-dots span{width:11px;height:11px;border-radius:50%;border:2px solid var(--white)}
.hero-dots span.on{background:var(--white)}

/* filters */
.filters{top:676px;height:164px}
.select{position:absolute;width:243px;height:42px;border:1px solid #c9c9c9;border-radius:3px;padding:0 14px;font-size:13.5px;color:#666;display:flex;align-items:center;justify-content:space-between}
.filters .btn{position:absolute;width:239px;height:42px;line-height:42px;border-radius:3px;left:860px;top:87px;display:flex;justify-content:space-between;padding:0 18px}

/* welcome */
.welcome{top:840px;height:277px}
.welcome p{position:absolute;left:190px;width:820px;top:136px;text-align:center;font-size:13px;line-height:23px}

/* testimonial */
.testimonial{top:1117px;height:253px;background:var(--band);text-align:center}
.stars{left:530px;top:40px;display:flex;gap:4px}
.testimonial blockquote{position:absolute;left:0;width:1200px;top:84px;font-style:italic;font-size:19px;color:#444}
.testimonial cite{position:absolute;left:0;width:1200px;top:126px;font-style:normal;font-weight:700;font-size:17px;color:var(--ink)}
.testimonial .btn{left:508px;top:168px;width:184px;height:44px;line-height:44px}

/* feature rows */
.features{top:1370px;height:836px}
.photo{position:absolute;border:1px solid #ddd}
.feature-title{position:absolute;font-family:"Lato",Arial,sans-serif;font-weight:900;font-size:34px;color:var(--ink)}
.feature-text{position:absolute;font-size:13.5px;line-height:24px}

/* cards */
.cards{position:absolute;left:104px;display:flex;gap:18px}
.card{width:236px;background:var(--white);border:1px solid #d8d8d8;position:relative}
.card .img{width:100%;display:block}
.arrow{position:absolute;width:38px;height:38px;border-radius:50%;border:1px solid #aaa;background:var(--white);display:flex;align-items:center;justify-content:center}

.journeys{top:2206px;height:457px;background:var(--band)}
.journey-body{height:80px;position:relative;padding:12px 10px}
.journey-body h3{font-family:"Open Sans",Arial,sans-serif;font-weight:700;font-size:17px;color:var(--ink)}
.journey-body .days{font-size:12px;color:var(--muted);display:flex;align-items:center;gap:5px;margin-top:4px}
.journey-body .from{position:absolute;right:10px;top:14px;font-size:12px;color:var(--muted)}
.journey-body .price{position:absolute;right:10px;top:30px;font-size:21px;color:var(--green);font-weight:600}

.experiences{top:2663px;height:475px;border-bottom:1px solid var(--line)}
.experience-label{height:66px;line-height:66px;text-align:center;font-weight:600;font-size:16px;color:var(--ink)}

/* marketing */
.marketing{top:3138px;height:649px}
.brochure{position:absolute;top:150px;width:225px;height:326px;border:1px solid #ccc}
.marketing .btn-outline{position:absolute;left:533px;top:545px;width:134px;height:46px;line-height:42px}

/* regions */
.regions{top:3787px;height:635px;background:var(--band)}
.region-body{height:167px;padding:16px 14px}
.region-body h3{font-family:"Open Sans",Arial,sans-serif;font-weight:700;font-size:18px;color:var(--ink);margin-bottom:10px}
.region-body p{font-size:13px;line-height:21px;color:var(--text)}
.regions .btn{position:absolute;left:532px;top:524px;width:136px;height:46px;line-height:46px}

/* partners */
.partners{top:4422px;height:232px}
.partner{position:absolute;top:72px;width:184px;height:83px;border:1px solid #d0d0d0;display:flex;align-items:center;justify-content:center;gap:10px;font-family:"Lato",Arial,sans-serif;font-weight:700;font-size:15px;color:#333}
.partner i{width:22px;height:22px;background:#333;border-radius:50%;display:block}

/* footer */
.footer{top:4654px;height:548px;background:var(--footer);color:var(--footer-text)}
.footer h4{position:absolute;top:58px;font-family:"Lato",Arial,sans-serif;font-weight:700;font-size:17px;color:var(--white)}
.footer ul{list-style:none;position:absolute;top:104px;font-size:13px;line-height:22px}
.footer .about{position:absolute;left:343px;top:104px;width:310px;font-size:13px;line-height:22px}
.footer .mailing-intro{position:absolute;left:690px;top:104px;width:210px;font-size:13px;line-height:20px}
.input{position:absolute;left:690px;width:205px;height:32px;background:var(--white);border-radius:2px;font-size:12px;color:#777;padding:0 10px;line-height:32px}
.footer .btn{position:absolute;left:690px;top:337px;width:118px;height:34px;line-height:34px;font-size:12px}
.footer .required{position:absolute;left:690px;top:383px;font-size:13px;font-style:italic}
.contact-list{position:absolute;left:929px;top:104px;font-size:13px;line-height:22px}
.contact-list div{display:flex;gap:8px;align-items:flex-start;margin-bottom:6px}
.footer .social{position:absolute;left:929px;top:306px;gap:8px}
.footer .social span{width:26px;height:26px;background:#3d3d3d;border:1px solid #666}
.badge{position:absolute;background:#e6e6e6;border:1px solid #bbb}
.footer .copy{position:absolute;left:0;width:1200px;top:472px;border-top:1px solid #444;padding-top:22px;text-align:center;font-size:13px}
</style>
</head>
<body>

<header class="sec header">
  <div class="abs brand-name">MARLOW</div>
  <div class="abs brand-sub">Pennant</div>
  <div class="abs header-phone">
    <svg width="16" height="16" viewBox="0 0 24 24"><path fill="#222" d="M6.6 10.8a15 15 0 0 0 6.6 6.6l2.2-2.2a1 1 0 0 1 1-.25 11.4 11.4 0 0 0 3.6.57 1 1 0 0 1 1 1V20a1 1 0 0 1-1 1A17 17 0 0 1 3 4a1 1 0 0 1 1-1h3.5a1 1 0 0 1 1 1c0 1.25.2 2.45.57 3.57a1 1 0 0 1-.25 1z"/></svg>
    0800 44 21 90
  </div>
  <div class="abs social"><span></span><span></span><span></span><span></span></div>
  <div class="abs btn">Newsletter Subscribe</div>
</header>

<nav class="sec nav">
  <ul>
    <li class="current">HOME</li><li>ABOUT US</li><li>OUR CRUISES</li><li>DESTINATIONS</li><li>EXCLUSIVE OFFERS</li><li>BROCHURES</li><li>OUR TEAM</li><li>CONTACT</li>
  </ul>
</nav>

<section class="sec hero" role="img" aria-label="Photo of a large cruise ship docked in a fjord with passengers on the quay">
  <h1>TRAVEL WITH PERSONALITY</h1>
  <div class="abs hero-search">
    <div class="field">
      <svg width="14" height="14" viewBox="0 0 24 24"><circle cx="10" cy="10" r="7" fill="none" stroke="#888" stroke-width="2.5"/><path d="M15 15l6 6" stroke="#888" stroke-width="2.5"/></svg>
      Where do you feel like going
    </div>
    <div class="go"><svg width="22" height="22" viewBox="0 0 24 24"><circle cx="10" cy="10" r="7" fill="none" stroke="#fff" stroke-width="3"/><path d="M15 15l6 6" stroke="#fff" stroke-width="3"/></svg></div>
  </div>
  <div class="abs hero-dots"><span class="on"></span><span></span><span></span><span></span></div>
</section>

<section class="sec filters">
  <div class="select" style="left:97px;top:28px">Any Destination <span>▾</span></div>
  <div class="select" style="left:354px;top:28px">Any Sailing Date <span>▾</span></div>
  <div class="select" style="left:607px;top:28px">Any Length <span>▾</span></div>
  <div class="select" style="left:860px;top:28px">Any Cruise Line <span>▾</span></div>
  <div class="select" style="left:97px;top:87px">Any Cruise Ship <span>▾</span></div>
  <div class="select" style="left:354px;top:87px">Any Departure Port <span>▾</span></div>
  <div class="select" style="left:607px;top:87px">Any Price Range <span>▾</span></div>
  <div class="btn">Search Cruises <span>▾</span></div>
</section>

<section class="sec welcome">
  <h2 class="section-title" style="top:70px">WELCOME TO MARLOW PENNANT</h2>
  <p>It takes years and many personal moments to know a place; its nooks and crannies, its people, how it all works. Our first-hand knowledge of our destinations, built over many years, shapes Marlow Pennant's personalised tailor-made and small group hosted travel experiences. This ensures comfortable, stylish and hassle-free experiences for our travellers.</p>
</section>

<section class="sec testimonial">
  <div class="abs stars">
    <svg width="140" height="24" viewBox="0 0 140 24"><g fill="#8bc34a"><path id="st" d="M12 1l3.2 7 7.6.8-5.7 5.1 1.6 7.5L12 17.6 5.3 21.4l1.6-7.5L1.2 8.8 8.8 8z"/><use href="#st" x="29"/><use href="#st" x="58"/><use href="#st" x="87"/><use href="#st" x="116"/></g></svg>
  </div>
  <blockquote>“Friendly reliable busted great to deal with.”</blockquote>
  <cite>M_Hadley, NSW</cite>
  <div class="abs btn">See All Reviews</div>
</section>

<section class="sec features">
  <div class="photo" role="img" aria-label="Photo of a polar bear resting on snow" style="left:104px;top:69px;width:427px;height:305px;background:linear-gradient(160deg,#dfe9f0,#b8c8d4)"></div>
  <h2 class="feature-title" style="left:593px;top:84px">SMALL SHIPS ARE BEST</h2>
  <p class="feature-text" style="left:593px;top:140px;width:510px">Up close and person is the way we love our cruise voyages.<br><br>Whether in the Mediterranean or the Canadian Arctic, small ships enable the discerning cruise traveller to get the best view in the world. Select from the many destination</p>
  <div class="abs btn-outline" style="left:593px;top:314px;width:196px;height:44px;line-height:40px">Discover Our Range</div>

  <h2 class="feature-title" style="left:98px;top:466px">YOU WON'T FIND IT ELSEWHERE</h2>
  <p class="feature-text" style="left:98px;top:524px;width:480px">With over 15 years experience in creating unique packages for the Australian cruise traveller, we like to think we know have an idea what you want. We aim for comfortable, unique hassle free experiences for our guests.</p>
  <div class="abs btn-outline" style="left:98px;top:673px;width:196px;height:44px;line-height:40px">Meet Our Team</div>
  <div class="photo" role="img" aria-label="Photo of an orangutan with its young among green leaves" style="left:669px;top:440px;width:430px;height:305px;background:linear-gradient(150deg,#6f9a3a,#3f6a22)"></div>
</section>

<section class="sec journeys">
  <h2 class="section-title" style="top:54px">FEATURED JOURNEYS</h2>
  <div class="arrow" style="left:31px;top:244px"><svg width="12" height="12" viewBox="0 0 12 12"><path d="M8 1L3 6l5 5" fill="none" stroke="#666" stroke-width="2"/></svg></div>
  <div class="arrow" style="left:1129px;top:244px"><svg width="12" height="12" viewBox="0 0 12 12"><path d="M4 1l5 5-5 5" fill="none" stroke="#666" stroke-width="2"/></svg></div>
  <div class="cards" style="top:135px">
    <div class="card"><div class="img" role="img" aria-label="Photo of a small expedition ship in a glacier fjord" style="height:173px;background:linear-gradient(170deg,#9fb8c8,#3f5f6e)"></div>
      <div class="journey-body"><h3>Amazon Cruise</h3><div class="days"><svg width="11" height="11" viewBox="0 0 12 12"><circle cx="6" cy="6" r="5" fill="none" stroke="#999" stroke-width="1.4"/><path d="M6 3v3h2.5" fill="none" stroke="#999" stroke-width="1.4"/></svg>4 Days / 3 Nights</div><span class="from">From</span><span class="price">$2470</span></div></div>
    <div class="card"><div class="img" role="img" aria-label="Photo of a river boat on a misty river" style="height:173px;background:linear-gradient(170deg,#c7d6dc,#5d7a70)"></div>
      <div class="journey-body"><h3>Amazon Cruise</h3><div class="days"><svg width="11" height="11" viewBox="0 0 12 12"><circle cx="6" cy="6" r="5" fill="none" stroke="#999" stroke-width="1.4"/><path d="M6 3v3h2.5" fill="none" stroke="#999" stroke-width="1.4"/></svg>4 Days / 3 Nights</div><span class="from">From</span><span class="price">$2470</span></div></div>
    <div class="card"><div class="img" role="img" aria-label="Photo of a cruise ship below snowy mountains" style="height:173px;background:linear-gradient(170deg,#7aa8d8,#2f5c86)"></div>
      <div class="journey-body"><h3>Amazon Cruise</h3><div class="days"><svg width="11" height="11" viewBox="0 0 12 12"><circle cx="6" cy="6" r="5" fill="none" stroke="#999" stroke-width="1.4"/><path d="M6 3v3h2.5" fill="none" stroke="#999" stroke-width="1.4"/></svg>4 Days / 3 Nights</div><span class="from">From</span><span class="price">$2470</span></div></div>
    <div class="card"><div class="img" role="img" aria-label="Photo of a red and white paddle steamer" style="height:173px;background:linear-gradient(170deg,#d9dde2,#a23a3a)"></div>
      <div class="journey-body"><h3>Amazon Cruise</h3><div class="days"><svg width="11" height="11" viewBox="0 0 12 12"><circle cx="6" cy="6" r="5" fill="none" stroke="#999" stroke-width="1.4"/><path d="M6 3v3h2.5" fill="none" stroke="#999" stroke-width="1.4"/></svg>4 Days / 3 Nights</div><span class="from">From</span><span class="price">$2470</span></div></div>
  </div>
</section>

<section class="sec experiences">
  <h2 class="section-title" style="top:84px">AMAZING RANGE OF EXPERIENCES</h2>
  <div class="arrow" style="left:31px;top:236px"><svg width="12" height="12" viewBox="0 0 12 12"><path d="M8 1L3 6l5 5" fill="none" stroke="#666" stroke-width="2"/></svg></div>
  <div class="arrow" style="left:1129px;top:236px"><svg width="12" height="12" viewBox="0 0 12 12"><path d="M4 1l5 5-5 5" fill="none" stroke="#666" stroke-width="2"/></svg></div>
  <div class="cards" style="top:163px">
    <div class="card"><div class="img" role="img" aria-label="Photo of a river boat passing an old castle" style="height:177px;background:linear-gradient(170deg,#6f9ccc,#6b4a34)"></div><div class="experience-label">River Cruises</div></div>
    <div class="card"><div class="img" role="img" aria-label="Photo of an expedition inflatable boat among icebergs" style="height:177px;background:linear-gradient(170deg,#a9cde2,#2f6f95)"></div><div class="experience-label">Expedition Cruises</div></div>
    <div class="card"><div class="img" role="img" aria-label="Photo of a sunset over the sea from a plane window" style="height:177px;background:linear-gradient(170deg,#f3b061,#5a3e6b)"></div><div class="experience-label">Fly Free Cruises</div></div>
    <div class="card"><div class="img" role="img" aria-label="Photo of two champagne glasses at sunset" style="height:177px;background:linear-gradient(170deg,#8ab6d8,#e2b768)"></div><div class="experience-label">Luxury Cruises</div></div>
  </div>
</section>

<section class="sec marketing">
  <h2 class="section-title" style="top:64px">RECENT MARKETING</h2>
  <div class="brochure" role="img" aria-label="Fly free to Europe brochure cover" style="left:198px;background:linear-gradient(180deg,#2e7fbf 0%,#2e7fbf 22%,#e9e6da 22%,#c8b69a 100%)"></div>
  <div class="brochure" role="img" aria-label="Celtic cruising brochure cover" style="left:489px;background:linear-gradient(180deg,#1f4f8f 0%,#1f4f8f 24%,#e8eef4 24%,#b7c9dc 100%)"></div>
  <div class="brochure" role="img" aria-label="Christmas markets brochure cover" style="left:773px;background:linear-gradient(180deg,#c62a2a 0%,#c62a2a 24%,#f2ece2 24%,#d6b7a0 100%)"></div>
  <div class="btn-outline">View All</div>
</section>

<section class="sec regions">
  <h2 class="section-title" style="top:56px">FEATURED REGIONS</h2>
  <div class="cards" style="top:132px">
    <div class="card"><div class="img" role="img" aria-label="Photo of zebras on the African savanna at sunset" style="height:180px;background:linear-gradient(170deg,#e2a04a,#6e4a22)"></div>
      <div class="region-body"><h3>Africa</h3><p>Nemo enim ipsam voluptatem quia voluptas sit aspernatur aut odit aut fugit, sed qu...</p></div></div>
    <div class="card"><div class="img" role="img" aria-label="Photo of limestone islands rising from a green bay" style="height:180px;background:linear-gradient(170deg,#a8c7d4,#3e6d5a)"></div>
      <div class="region-body"><h3>Asia</h3><p>Nemo enim ipsam voluptatem quia voluptas sit aspernatur aut odit aut fugit, sed qu...</p></div></div>
    <div class="card"><div class="img" role="img" aria-label="Photo of a mountain lake with pine forest" style="height:180px;background:linear-gradient(170deg,#9dbbd8,#4d6a4a)"></div>
      <div class="region-body"><h3>Canada &amp; USA</h3><p>Nemo enim ipsam voluptatem quia voluptas sit aspernatur aut odit aut fugit, sed qu...</p></div></div>
    <div class="card"><div class="img" role="img" aria-label="Photo of a bright tropical flower" style="height:180px;background:linear-gradient(170deg,#e0592a,#2f6b3a)"></div>
      <div class="region-body"><h3>Central America</h3><p>Nemo enim ipsam voluptatem quia voluptas sit aspernatur aut odit aut fugit, sed qu...</p></div></div>
  </div>
  <div class="btn">View All</div>
</section>

<section class="sec partners">
  <div class="arrow" style="left:31px;top:94px"><svg width="12" height="12" viewBox="0 0 12 12"><path d="M8 1L3 6l5 5" fill="none" stroke="#666" stroke-width="2"/></svg></div>
  <div class="arrow" style="left:1129px;top:94px"><svg width="12" height="12" viewBox="0 0 12 12"><path d="M4 1l5 5-5 5" fill="none" stroke="#666" stroke-width="2"/></svg></div>
  <div class="partner" style="left:104px">Harbourline Hotels</div>
  <div class="partner" style="left:306px"><i></i>Wildcare Fund</div>
  <div class="partner" style="left:508px">Coastal Wildlife Park</div>
  <div class="partner" style="left:710px">Palmview Collective</div>
  <div class="partner" style="left:912px;width:190px"><i></i>Meridian Voyages</div>
</section>

<footer class="sec footer">
  <h4 style="left:98px">Discover Marlow Pennant</h4>
  <ul style="left:98px"><li>Home</li><li>Vested</li><li>Independent</li><li>Brochures</li><li>Careers</li><li>Terms</li></ul>
  <ul style="left:210px"><li>Destinations</li><li>Cruise</li><li>Special Offers</li><li>Meet Our Team</li><li>Contact</li><li>Privacy Policy</li></ul>

  <h4 style="left:343px">Welcome to Our World</h4>
  <p class="about">It takes years and many personal moments to know a place, its nooks and crannies, its people, how it all works. Our first-hand knowledge of our destinations, built over many years, shapes Marlow Pennant's personalised tailor-made and small-group hosted travel experiences. This ensures comfortable, stylish and hassle-free experiences for our travellers.</p>
  <div class="badge" style="left:349px;top:300px;width:108px;height:50px"></div>
  <div class="badge" style="left:468px;top:300px;width:112px;height:50px"></div>
  <div class="badge" style="left:349px;top:358px;width:108px;height:50px"></div>

  <h4 style="left:690px">Mailing List</h4>
  <p class="mailing-intro">Sign up for our mailing list to get updates and offers.</p>
  <div class="input" style="top:177px">Email Address</div>
  <div class="input" style="top:232px">First Name</div>
  <div class="input" style="top:287px">Last Name</div>
  <div class="btn">Subscribe</div>
  <div class="required">* required</div>

  <div class="contact-list">
    <div><svg width="12" height="14" viewBox="0 0 24 24"><path fill="#cfcfcf" d="M6.6 10.8a15 15 0 0 0 6.6 6.6l2.2-2.2a1 1 0 0 1 1-.25 11.4 11.4 0 0 0 3.6.57 1 1 0 0 1 1 1V20a1 1 0 0 1-1 1A17 17 0 0 1 3 4a1 1 0 0 1 1-1h3.5a1 1 0 0 1 1 1c0 1.25.2 2.45.57 3.57a1 1 0 0 1-.25 1z"/></svg>0800 44 21 90</div>
    <div><svg width="12" height="14" viewBox="0 0 24 24"><path fill="#cfcfcf" d="M6.6 10.8a15 15 0 0 0 6.6 6.6l2.2-2.2a1 1 0 0 1 1-.25 11.4 11.4 0 0 0 3.6.57 1 1 0 0 1 1 1V20a1 1 0 0 1-1 1A17 17 0 0 1 3 4a1 1 0 0 1 1-1h3.5a1 1 0 0 1 1 1c0 1.25.2 2.45.57 3.57a1 1 0 0 1-.25 1z"/></svg>09 555 0142</div>
    <div><svg width="12" height="14" viewBox="0 0 24 24"><rect x="3" y="4" width="18" height="16" fill="none" stroke="#cfcfcf" stroke-width="2"/><path d="M7 9h10M7 14h6" stroke="#cfcfcf" stroke-width="2"/></svg>09 555 0143</div>
    <div><svg width="12" height="14" viewBox="0 0 24 24"><rect x="2" y="5" width="20" height="14" fill="none" stroke="#cfcfcf" stroke-width="2"/><path d="M2 6l10 7 10-7" fill="none" stroke="#cfcfcf" stroke-width="2"/></svg>info@marlowpennant.example</div>
    <div><svg width="12" height="16" viewBox="0 0 24 24"><path fill="#cfcfcf" d="M12 2a7 7 0 0 0-7 7c0 5 7 13 7 13s7-8 7-13a7 7 0 0 0-7-7zm0 9.5A2.5 2.5 0 1 1 12 6.5a2.5 2.5 0 0 1 0 5z"/></svg>Level 2, 18 Harbour<br>Lane, Quay District<br>Sydney NSW 2000</div>
  </div>
  <div class="social"><span></span><span></span><span></span><span></span></div>
  <div class="badge" style="left:929px;top:354px;width:171px;height:70px"></div>

  <div class="copy">© Marlow Pennant 2007-2018. All Rights Reserved</div>
</footer>

</body>
</html>
```